Brightwave Travel and Tours

Hotel Reservations
Airline Ticketing
Day Tour

My business is a Travel agency. My services are issuing domestic and international tickets. Book room/hotel reservations local/international.
My color preference is apple green/orange/red/blue.
Images of beaches, tickets,luggage.

```html
<!DOCTYPE html>
<html lang="en">
<head>
<meta charset="UTF-8">
<title>Brightwave Travel and Tours – Business Card</title>
<link href="https://fonts.googleapis.com/css2?family=Arimo:wght@400;700&display=swap" rel="stylesheet">
<style>
  :root {
    --page-bg: #e9ebee;
    --card-white: #ffffff;
    --brand-teal: #157fa3;
    --brand-teal-dark: #0f6d8e;
    --brand-sky: #4fc0ea;
    --text-dark: #3a3f44;
    --text-light: #ffffff;
  }
  * { margin: 0; padding: 0; box-sizing: border-box; }
  html, body {
    width: 1200px; height: 750px; overflow: hidden;
    background: var(--page-bg);
    font-family: "Arimo", Arial, sans-serif;
  }
  .canvas {
    width: 1200px; height: 750px;
    display: flex; align-items: center; justify-content: center; gap: 40px;
  }
  .card {
    width: 540px; height: 308px;
    background: var(--card-white);
    position: relative; overflow: hidden;
    box-shadow: 0 6px 18px rgba(0,0,0,0.18);
  }

  /* Front */
  .card-front {
    display: flex; flex-direction: column; align-items: center; justify-content: center;
  }
  .brand-lockup { display: flex; align-items: center; gap: 14px; }
  .brand-dot {
    width: 58px; height: 58px; border-radius: 50%;
    background: var(--brand-sky);
  }
  .brand-name {
    color: var(--brand-teal-dark); font-weight: 700;
    font-size: 26px; line-height: 1.1; letter-spacing: 1px; text-transform: uppercase;
  }
  .services {
    margin-top: 34px; font-size: 14px; color: var(--text-dark);
  }
  .services .sep { margin: 0 6px; color: var(--brand-teal); }

  /* Back */
  .band {
    position: absolute; left: 0; right: 0; top: 48px; height: 200px;
    background: var(--brand-teal);
  }
  .contact {
    position: absolute; left: 34px; top: 66px; color: var(--text-light);
  }
  .contact-name { font-size: 20px; font-weight: 700; }
  .contact-role { font-size: 14px; margin-top: 3px; }
  .contact-address { font-size: 13px; line-height: 1.35; margin-top: 4px; }
  .contact-list { list-style: none; margin-top: 6px; font-size: 13px; }
  .contact-list li { display: flex; align-items: center; gap: 8px; line-height: 19px; }
  .contact-list svg { width: 13px; height: 13px; fill: var(--text-light); flex: none; }
  .back-brand {
    position: absolute; right: 34px; top: 82px;
    display: flex; flex-direction: column; align-items: center; gap: 12px;
  }
  .back-brand .brand-dot {
    width: 96px; height: 96px; background: var(--brand-sky);
    border: 4px solid var(--text-light);
  }
  .back-brand .brand-name { color: var(--text-light); font-size: 15px; letter-spacing: 1px; }
</style>
</head>
<body>
<main class="canvas">
  <section class="card card-front">
    <div class="brand-lockup">
      <span class="brand-dot"></span>
      <p class="brand-name">Brightwave<br>Travel and Tours</p>
    </div>
    <p class="services">Hotel Reservations<span class="sep">•</span>Airline Ticketing<span class="sep">•</span>Day Tour</p>
  </section>

  <section class="card card-back">
    <div class="band"></div>
    <div class="contact">
      <p class="contact-name">Marco Ellison</p>
      <p class="contact-role">President</p>
      <p class="contact-address">4127 Harbor Crest Lane<br>Seabrook, NJ 08302</p>
      <ul class="contact-list">
        <li><svg viewBox="0 0 16 16"><path d="M3 1h3l1.5 4-2 1.2a9 9 0 0 0 4.3 4.3L11 8.5l4 1.5v3a2 2 0 0 1-2 2A13 13 0 0 1 1 3a2 2 0 0 1 2-2z"/></svg>521 6408 3197</li>
        <li><svg viewBox="0 0 16 16"><path d="M4 0h8a1 1 0 0 1 1 1v14a1 1 0 0 1-1 1H4a1 1 0 0 1-1-1V1a1 1 0 0 1 1-1zm1 2v10h6V2zm3 11a1 1 0 1 0 0 2 1 1 0 0 0 0-2z"/></svg>847 2916 5043</li>
        <li><svg viewBox="0 0 16 16"><path d="M4 0h7v5H4zM1 6h14v8H1zm3 3v3h8V9z"/></svg>832 5174 2689</li>
        <li><svg viewBox="0 0 16 16"><path d="M0 3h16v10H0zm1.5 1.2L8 9l6.5-4.8V4h-13z"/></svg>marco@brightwavetours.com</li>
        <li><svg viewBox="0 0 16 16"><path d="M8 0a8 8 0 1 0 0 16A8 8 0 0 0 8 0zm0 2a6 6 0 0 1 5.7 4H10a9 9 0 0 0-1.2-3.9A6 6 0 0 1 8 2zM2.3 10h3.2a12 12 0 0 0 .9 3.8A6 6 0 0 1 2.3 10zm0-4a6 6 0 0 1 4.1-3.8A12 12 0 0 0 5.5 6zM7.5 10h1a9 9 0 0 1-.5 3.5 9 9 0 0 1-.5-3.5zm0-4A9 9 0 0 1 8 2.5 9 9 0 0 1 8.5 6zm2.1 7.8A12 12 0 0 0 10.5 10h3.2a6 6 0 0 1-4.1 3.8z"/></svg>www.brightwavetours.com</li>
      </ul>
    </div>
    <div class="back-brand">
      <span class="brand-dot"></span>
      <p class="brand-name">Brightwave</p>
    </div>
  </section>
</main>
</body>
</html>
```